Modern and sophisticated web design for architect/designer

Lumo Vant is a Building Design & Drafting studio based in Nedlands Western Australia, providing a high quality and complete client service from concept design through Council planning approvals and building licenses to construction drawings for kitchens and bathrooms, extensions, additions, renovations and new homes.

Lumo Vant is looking for a new qwerty design that *is different from a normal* 2/3 column website. The website design must be very arty, clean and catchy. This design needs to be very different and must not look like a downloadable template.

The design must be able to display a lot of photos for the different projects.

The design must comply with W3C standards (i.e. use of fonts) and must be delivered to us in A PSD layered format.

Here are a couple of example website designs that exemplify what I am after:
1) http://www.prtd.com.au/
2) http://www.martinholsbyarchitect.com/en/
3) http://veromiks.com/

I particularly like numbers 1 and 2. The third, Veromiks, jumps around a little between pages as it is actually several companies. I prefer the page design to remain steady if possible.

I like the very clever nature of number 1 (PRTD). It captures the interest, although slightly gimmicky, however I think it doesn't overpower. Its modern, and visual.

I like the clean elegant design of number 2 (Holsby), it simply delivers everything necessary in a clear intelligent manner, its attractive, menu is clever simple to use and attractive.

I would be very happy to have either of these websites.

here is another one:
4) http://www.tqarchitect.com.au/

Although this is similarly elegant, it appears quite dated. I don't like the thumbnails that you click on in the gallery, its quite clumsy. It looks minimalist, and IS minimalist, doesn't look like there is much option to expand other than changing the pictures.

If you look at my own website:
http://www.lumovant.com.au

I designed and built it myself without any skills or experience. I had to use a generic photo album generator which was worse than useless, the point I am trying to make is I tried to make the menu system a little unusual, I tried to keep the pages neat and tidy, and totally used the "black website" method. However I am more inclined to go with the lighter/white pages of (1) and (2) above because they tend to show photos better.

Dear Designers. 

ArtHive Administration has worked to provide a more comprehensive brief. Please review the amended description. 

Kind Regards, Wesley. 

Target Market(s)

Target market is people who are looking to renovate their home

Industry/Entity Type

Construction

Requirements
Must have
• The brief is to design a visual modern, elegant, sophisticated website for a small scale designer/photographer/architect that looks itself like it is designed. Not off the shelf, simple and dated. Basically the design itself has to exemplify me, it has to say "this guy is a designer, and he is good at it".

```html
<!DOCTYPE html>
<html lang="en">
<head>
<meta charset="utf-8">
<title>Lumo Vant — Building Design &amp; Drafting</title>
<link rel="stylesheet" href="https://fonts.googleapis.com/css2?family=Open+Sans:wght@400;600;700&display=swap">
<style>
  :root {
    --sidebar: #3a3834;
    --sidebar-active: #57544f;
    --footer: #000000;
    --page: #ffffff;
    --white: #ffffff;
    --muted: #8a8782;
    --muted-light: #9a968f;
    --tweet-blue: #5b8fc9;
    --accent-red: #be0f16;
    --accent-orange: #f57c0a;
    --logo-ink: #3d3d3d;
    --footer-text: #9d9d9d;
  }
  * { margin: 0; padding: 0; box-sizing: border-box; }
  html, body { width: 1200px; height: 1020px; overflow: hidden; }
  body {
    position: relative;
    background: var(--page);
    font-family: "Open Sans", Arial, sans-serif;
  }

  /* Sidebar */
  .sidebar {
    position: absolute; left: 0; top: 0;
    width: 263px; height: 977px;
    background: var(--sidebar);
  }
  .main-nav { position: absolute; top: 232px; left: 0; width: 263px; list-style: none; }
  .main-nav li {
    height: 28.8px; line-height: 28.8px;
    text-align: center; color: var(--white);
    font-size: 14.5px; font-weight: 600;
  }
  .main-nav li.is-active { background: var(--sidebar-active); height: 26px; line-height: 26px; margin-bottom: 2.8px; }

  .sidebar-heading {
    position: absolute; color: var(--white);
    font-size: 17px; font-weight: 700; letter-spacing: 0.2px;
  }
  .tweets-heading { left: 30px; top: 422px; }
  .tweet { position: absolute; left: 26px; width: 220px; }
  .tweet-icon { position: absolute; left: 0; top: 0; }
  .tweet-text {
    position: absolute; left: 47px; top: -5px; width: 200px;
    color: var(--muted); font-size: 13px; line-height: 21.6px;
  }
  .tweet-1 { top: 458px; }
  .tweet-2 { top: 552px; }

  .newsletter-heading { left: 20px; top: 687px; }
  .newsletter-intro {
    position: absolute; left: 20px; top: 714px; width: 230px;
    color: var(--muted-light); font-size: 17.5px; line-height: 21px;
    white-space: nowrap;
  }
  .newsletter-input {
    position: absolute; left: 17px; top: 768px;
    width: 222px; height: 25px;
    background: #fbfbf8; border: 1px solid #ccc;
    color: #a6a39c; font-size: 12px; line-height: 23px; padding-left: 8px;
  }
  .newsletter-submit {
    position: absolute; left: 19px; top: 808px;
    width: 147px; height: 23px;
    border: 1px solid var(--white);
    color: var(--white); font-size: 11.5px; line-height: 21px; text-align: center;
  }

  /* Brand */
  .brand {
    position: absolute; left: 346px; top: 104px;
    display: flex; align-items: center; gap: 14px;
  }
  .brand-mark { width: 30px; height: 30px; background: var(--logo-ink); }
  .brand-name {
    color: var(--logo-ink); font-size: 40px; font-weight: 700;
    letter-spacing: 8px; line-height: 1;
  }

  /* Gallery */
  .photo { position: absolute; }
  .photo-studio   { left: 764px; top: 74px;  width: 177px; height: 118px; background: linear-gradient(135deg, #c9ccd6, #5a5e72 60%, #2a2c3a); }
  .photo-kitchen  { left: 340px; top: 204px; width: 177px; height: 162px; background: linear-gradient(160deg, #6b4a3a, #3a2a22 60%, #8a5b3c); }
  .photo-feature  { left: 527px; top: 204px; width: 414px; height: 416px; background: linear-gradient(180deg, #2f5fa8 0%, #2a3a55 30%, #8a5a22 55%, #c98a2a 70%, #3d3a22 100%); }
  .photo-facade   { left: 952px; top: 204px; width: 248px; height: 163px; background: linear-gradient(180deg, #6fa2e0 0%, #b9c8d8 40%, #7a6e62 70%, #5a7a3a 100%); }
  .photo-hallway  { left: 264px; top: 373px; width: 253px; height: 168px; background: linear-gradient(90deg, #4a2e20, #a66a3a 45%, #3a2418 80%, #8a5a38); }
  .photo-balcony  { left: 950px; top: 372px; width: 110px; height: 166px; background: linear-gradient(180deg, #5a7fbf 0%, #9aa6b8 50%, #3f6a3a 80%, #a7a29b 100%); }
  .photo-cooktop  { left: 950px; top: 544px; width: 177px; height: 118px; background: linear-gradient(180deg, #5a2a20 0%, #8a4a32 45%, #c9b79f 75%, #6a5a48 100%); }
  .photo-garden   { left: 527px; top: 629px; width: 253px; height: 163px; background: linear-gradient(135deg, #1f2a1a, #7a5a2a 45%, #c9a05a 60%, #2a3a1f 100%); }
  .photo-strip    { left: 787px; top: 629px; width: 106px; height: 163px; background: linear-gradient(90deg, #3a4a6a 0, #3a4a6a 18px, #f6f6f6 18px, #f9f9f9 100%); }
  .photo-terrace  { left: 784px; top: 800px; width: 174px; height: 124px; background: linear-gradient(180deg, #4f8ad8 0%, #a9b8c8 45%, #6a6058 70%, #4e7a36 100%); }

  .feature-card {
    position: absolute; color: var(--white); text-align: center;
  }
  .feature-card h2 { font-weight: 700; text-transform: uppercase; }
  .feature-card p {
    font-size: 9.8px; line-height: 16px; letter-spacing: -0.15px;
    white-space: nowrap;
  }
  .card-kitchen {
    left: 292px; top: 548px; width: 225px; height: 170px;
    background: var(--accent-red); padding: 34px 0 0;
  }
  .card-kitchen h2 { font-size: 20px; line-height: 22px; margin-bottom: 6px; }
  .card-living {
    left: 551px; top: 802px; width: 224px; height: 136px;
    background: var(--accent-orange); padding: 18px 0 0;
  }
  .card-living h2 { font-size: 21px; line-height: 27px; margin-bottom: 3px; }

  /* Footer */
  .site-footer {
    position: absolute; left: 0; top: 977px;
    width: 1200px; height: 43px; background: var(--footer);
    color: var(--footer-text); font-size: 13.5px; line-height: 43px; text-align: center;
    padding-left: 50px;
  }
</style>
</head>
<body>

<aside class="sidebar">
  <ul class="main-nav">
    <li class="is-active">HOME</li>
    <li>GALLERY</li>
    <li>PORTFOLIO</li>
    <li>BLOG</li>
    <li>CONTACTS</li>
  </ul>

  <h3 class="sidebar-heading tweets-heading">RECENT TWEETS</h3>
  <div class="tweet tweet-1">
    <svg class="tweet-icon" width="32" height="32" viewBox="0 0 32 32" aria-hidden="true"><circle cx="16" cy="16" r="15" fill="var(--tweet-blue)"/></svg>
    <p class="tweet-text">Lorem ipsum dolor&nbsp; dolor adipiscing elit. Niih&nbsp; dolor cursrtus a, elefend.</p>
  </div>
  <div class="tweet tweet-2">
    <svg class="tweet-icon" width="32" height="32" viewBox="0 0 32 32" aria-hidden="true"><circle cx="16" cy="16" r="15" fill="var(--tweet-blue)"/></svg>
    <p class="tweet-text">Lorem ipsum dolor&nbsp; dolor adipiscing elit. Niih&nbsp; dolor cursrtus a, elefend.</p>
  </div>

  <h3 class="sidebar-heading newsletter-heading">NEWSLETTER SIGNUP</h3>
  <p class="newsletter-intro">Lorem ipsum sit adipisci<br>ng elit.</p>
  <div class="newsletter-input">YOUR E-MAIL</div>
  <div class="newsletter-submit">SUBMIT EMAIL ADDRESS</div>
</aside>

<header class="brand">
  <span class="brand-mark"></span>
  <span class="brand-name">LUMO VANT</span>
</header>

<main class="gallery">
  <div class="photo photo-studio" role="img" aria-label="Modern glass and steel studio interior"></div>
  <div class="photo photo-kitchen" role="img" aria-label="Warm-lit kitchen with wine rack"></div>
  <div class="photo photo-feature" role="img" aria-label="Stone-clad home lit at dusk with landscaped garden"></div>
  <div class="photo photo-facade" role="img" aria-label="Two-storey modern house with glass balconies"></div>
  <div class="photo photo-hallway" role="img" aria-label="Timber and stone entry hallway"></div>
  <div class="photo photo-balcony" role="img" aria-label="Balcony railing detail of a modern house"></div>
  <div class="photo photo-cooktop" role="img" aria-label="Kitchen benchtop with brick splashback"></div>
  <div class="photo photo-garden" role="img" aria-label="Lit garden steps and timber deck at night"></div>
  <div class="photo photo-strip" role="img" aria-label="Bright interior wall detail"></div>
  <div class="photo photo-terrace" role="img" aria-label="Modern house exterior with garden"></div>

  <section class="feature-card card-kitchen">
    <h2>Moderenize<br>Kichen</h2>
    <p>Lorem ipsum dolor sit amet, consectetur<br>adipiscing elit. Niihunclorem est, eleifend<br>cursrtus a, elefend in nunc. Nulla fagcigisi.</p>
  </section>

  <section class="feature-card card-living">
    <h2>Choose a best<br>way of living</h2>
    <p>Lorem ipsum dolor sit amet, consectetur<br>adipiscing elit. Niihunclorem est, eleifend<br>cursrtus a, elefend in nunc. Nulla fagcigisi.</p>
  </section>
</main>

<footer class="site-footer">COPYRIGHT © LUMOVANT ALL RIGHT RESERVED.</footer>

</body>
</html>
```